North Fern Holdings Business Card

A business card design to accompany the logo design you completed on Artisan Hive. We are open to your proposals. I did add one idea below that might work, but we aren't married to the idea. The company is a real estate services company. Clientele are typically high net worth individuals, executive level employment or owners of their own company, 30-60 years old.

Our 1 (bad?) idea: double sided card; One side landscape with logo and word mark. Other side Portrait with the logo only (oversize watermark maybe?). Somewhere add text of Name (Marcus Pellington), Title (Principal), phone # (949-555-0173) and email address (marcus@northfernhq.com). There would be a second design with my wife's name, number and email in place of mine.

Again totally open to ideas here.

Industry/Entity Type

Real Estate

```html
<!DOCTYPE html>
<html lang="en">
<head>
<meta charset="utf-8">
<title>North Fern Holdings – Business Card</title>
<link rel="stylesheet" href="https://fonts.googleapis.com/css2?family=Cinzel:wght@400&family=Gelasio:wght@400&family=Arimo:wght@400&display=swap">
<style>
  :root {
    --sage: #66935a;
    --paper: #ffffff;
    --backdrop: #000000;
  }
  * { margin: 0; padding: 0; box-sizing: border-box; }
  html, body {
    width: 1000px;
    height: 1200px;
    overflow: hidden;
    background: var(--backdrop);
  }
  .canvas { position: relative; width: 1000px; height: 1200px; }

  .card { position: absolute; background: var(--paper); overflow: hidden; }
  .card--front { left: 67px; top: 79px; width: 863px; height: 504px; }
  .card--back  { left: 68px; top: 630px; width: 863px; height: 505px; }

  .band { position: absolute; left: 0; width: 100%; background: var(--sage); }
  .card--front .band--top    { top: 0; height: 151px; }
  .card--front .band--bottom { top: 354px; height: 150px; }
  .card--back .band--middle  { top: 171px; height: 182px; }

  /* Front wordmark */
  .wordmark {
    position: absolute;
    left: 0; top: 151px; width: 100%; height: 203px;
    display: flex; align-items: center; justify-content: center; gap: 34px;
  }
  .wordmark__square {
    width: 58px; height: 58px; background: var(--sage);
  }
  .wordmark__name {
    font-family: "Cinzel", "Trajan Pro", serif;
    font-weight: 400;
    font-size: 50px;
    line-height: 1.05;
    color: var(--sage);
    letter-spacing: 1px;
  }

  /* Back: mark placeholder */
  .mark {
    position: absolute;
    left: 62px; top: 75px;
    width: 312px; height: 312px;
    border-radius: 50%;
    background: var(--sage);
    border: 10px solid var(--paper);
    display: flex; align-items: center; justify-content: center;
    text-align: center;
  }
  .mark__name {
    font-family: "Cinzel", "Trajan Pro", serif;
    font-weight: 400;
    font-size: 30px;
    line-height: 1.2;
    color: var(--paper);
  }

  .holder {
    position: absolute;
    right: 54px; top: 218px;
    text-align: right;
    color: var(--paper);
    font-family: "Gelasio", Georgia, serif;
  }
  .holder__name { font-size: 31px; line-height: 1.2; }
  .holder__title { font-size: 21px; line-height: 1.2; margin-top: 10px; }

  .contact {
    position: absolute;
    top: 362px; left: 299px;
    display: flex; align-items: baseline; gap: 48px;
    color: var(--sage);
  }
  .contact__email { font-family: "Gelasio", Georgia, serif; font-size: 24px; }
  .contact__phone { font-family: "Arimo", Arial, sans-serif; font-size: 18px; }
</style>
</head>
<body>
<main class="canvas">
  <section class="card card--front" aria-label="Card front">
    <div class="band band--top"></div>
    <div class="wordmark">
      <span class="wordmark__square" aria-hidden="true"></span>
      <h1 class="wordmark__name">North Fern<br>Holdings</h1>
    </div>
    <div class="band band--bottom"></div>
  </section>

  <section class="card card--back" aria-label="Card back">
    <div class="band band--middle"></div>
    <div class="mark">
      <span class="mark__name">North Fern<br>Holdings</span>
    </div>
    <div class="holder">
      <p class="holder__name">Marcus Pellington</p>
      <p class="holder__title">(Principal)</p>
    </div>
    <div class="contact">
      <span class="contact__email">marcus@northfernhq.com</span>
      <span class="contact__phone">Tel- 949-555-0173</span>
    </div>
  </section>
</main>
</body>
</html>
```